Progressive/contemporary business card design for successful Startups as a Service Company

New logo launched in 2020. New website launched in 2021. Now that COVID is (mostly) behind us, I'm networking with more people and need a business card that matches the company/logo design aesthetic.

```html
<!DOCTYPE html>
<html lang="en">
<head>
<meta charset="utf-8">
<title>Vantori Business Card</title>
<link href="https://fonts.googleapis.com/css2?family=Montserrat:wght@400;500;700&display=swap" rel="stylesheet">
<style>
  :root {
    --page-bg: #9a9a9a;
    --card-white: #ffffff;
    --ink: #222222;
    --brand-slate: #435469;
    --accent-orange: #f15a24;
    --green-dark: #2e9e48;
    --green-mid: #5bb84a;
    --green-light: #a6ce39;
  }
  * { margin: 0; padding: 0; box-sizing: border-box; }
  html, body {
    width: 1021px; height: 1200px; overflow: hidden;
    background: var(--page-bg);
    font-family: "Montserrat", sans-serif;
    color: var(--ink);
  }
  .canvas { position: relative; width: 1021px; height: 1200px; }

  .card { position: absolute; width: 753px; height: 429px; }
  .card-front { left: 134px; top: 119px; background: var(--card-white); }
  .card-back {
    left: 131px; top: 651px;
    background: linear-gradient(30deg, var(--green-dark) 0%, var(--green-mid) 45%, var(--green-light) 100%);
  }

  .wordmark {
    position: absolute; left: 30px; top: 66px;
    font-size: 50px; font-weight: 500; letter-spacing: 17px;
    color: var(--brand-slate); line-height: 1;
  }

  .person-name {
    position: absolute; left: 31px; top: 233px;
    font-size: 26px; font-weight: 700; line-height: 1;
    background: linear-gradient(90deg, var(--green-dark), var(--green-light));
    -webkit-background-clip: text; background-clip: text; color: transparent;
  }
  .person-role {
    position: absolute; left: 31px; top: 263px;
    font-size: 18px; font-weight: 400;
  }

  .contact-list {
    position: absolute; left: 30px; top: 313px;
    list-style: none; font-size: 18.5px; line-height: 22.7px;
  }
  .contact-list li { display: flex; align-items: center; gap: 6px; }
  .contact-list svg { width: 13px; height: 13px; flex: none; }

  .address-divider {
    position: absolute; left: 282px; top: 364px;
    width: 2px; height: 35px; background: var(--green-mid);
  }
  .address {
    position: absolute; left: 301px; top: 358px;
    font-size: 18.5px; line-height: 22.7px; font-style: normal;
  }

  .back-name {
    position: absolute; inset: 0;
    display: flex; align-items: center; justify-content: center;
    font-size: 44px; font-weight: 500; letter-spacing: 14px;
    color: var(--card-white);
  }
</style>
</head>
<body>
<main class="canvas">
  <section class="card card-front">
    <div class="wordmark">VANTORI</div>

    <h1 class="person-name">DANIEL HARPER</h1>
    <p class="person-role">Owner/CEO</p>

    <ul class="contact-list">
      <li>
        <svg viewBox="0 0 14 14" aria-hidden="true"><rect x="3" y="0.8" width="8" height="12.4" rx="1.5" fill="none" stroke="var(--accent-orange)" stroke-width="1.4"/><circle cx="7" cy="10.8" r="0.9" fill="var(--accent-orange)"/></svg>
        555-318-2047
      </li>
      <li>
        <svg viewBox="0 0 14 14" aria-hidden="true"><path d="M3 1 L5.5 3.8 L4.3 5.3 Q5.5 8.2 8.7 9.7 L10.2 8.5 L13 11 L11.2 13 Q5.5 12.5 1 3 Z" fill="var(--accent-orange)"/></svg>
        555-318-2047
      </li>
      <li>
        <svg viewBox="0 0 14 14" aria-hidden="true"><rect x="0.5" y="2.5" width="13" height="9" fill="var(--accent-orange)"/><path d="M0.5 2.5 L7 7.5 L13.5 2.5 M0.5 11.5 L5 6.5 M13.5 11.5 L9 6.5" fill="none" stroke="#fff" stroke-width="1"/></svg>
        hello@vantori.com
      </li>
      <li>
        <svg viewBox="0 0 14 14" aria-hidden="true"><circle cx="7" cy="7" r="6.3" fill="var(--accent-orange)"/><path d="M3 4 Q5 3 6 5 Q5 7 3.5 7.5 M8 10 Q9 8 11 9" fill="none" stroke="#fff" stroke-width="1.2"/></svg>
        www.vantori.com
      </li>
    </ul>

    <span class="address-divider"></span>
    <address class="address">
      1480 W Harbor street<br>
      Maple County name 7714
    </address>
  </section>

  <section class="card card-back">
    <div class="back-name">VANTORI</div>
  </section>
</main>
</body>
</html>
```